New bussiness card, using company logo.
Lachlan Voss
Manager/Director
Birch Property Developments
Po Box 4657
Thuringowa Central
Qld
0455 386 218
lachlan@birchpropertydevelopments
eye catching, vibrant colours, professional

```html
<!DOCTYPE html>
<html lang="en">
<head>
<meta charset="utf-8">
<title>Lachlan Voss – Business Card</title>
<link href="https://fonts.googleapis.com/css2?family=Arimo:wght@400;700&display=swap" rel="stylesheet">
<style>
  :root {
    --page-bg: #ffffff;
    --card-bg: #ffffff;
    --card-edge: #d4d4d4;
    --ink-slate: #3e4b53;
    --brand-red: #e2001a;
  }
  html, body {
    margin: 0;
    padding: 0;
    width: 1200px;
    height: 1000px;
    overflow: hidden;
    background: var(--page-bg);
  }
  .card {
    position: absolute;
    left: 98px;
    top: 175px;
    width: 1005px;
    height: 652px;
    background: var(--card-bg);
    border: 1px solid var(--card-edge);
    box-sizing: border-box;
    font-family: "Arimo", Arial, sans-serif;
    color: var(--ink-slate);
  }
  .company {
    position: absolute;
    left: 400px;
    top: 60px;
    display: flex;
    align-items: center;
    gap: 12px;
    margin: 0;
    font-weight: 700;
    font-size: 22px;
    letter-spacing: 0.5px;
    color: var(--ink-slate);
    white-space: nowrap;
  }
  .company-mark {
    width: 18px;
    height: 18px;
    background: var(--brand-red);
  }
  .name-line {
    position: absolute;
    top: 270px;
    left: 0;
    right: 0;
    height: 56px;
  }
  .first-name {
    position: absolute;
    right: 623px;
    bottom: 8px;
    margin: 0;
    font-weight: 700;
    font-size: 44px;
    letter-spacing: 1px;
    color: var(--ink-slate);
    line-height: 1;
    white-space: nowrap;
  }
  .surname-group {
    position: absolute;
    left: 400px;
    bottom: 8px;
    display: flex;
    align-items: baseline;
    white-space: nowrap;
  }
  .surname {
    font-weight: 700;
    font-size: 44px;
    color: var(--brand-red);
    line-height: 1;
  }
  .job-title {
    margin-left: 16px;
    font-weight: 400;
    font-size: 32px;
    letter-spacing: 1px;
    color: var(--ink-slate);
    line-height: 1;
  }
  .accent-rule {
    position: absolute;
    left: 400px;
    right: 0;
    top: 323px;
    height: 6px;
    background: var(--brand-red);
  }
  .contact {
    position: absolute;
    left: 400px;
    top: 360px;
    margin: 0;
    font-style: normal;
    font-size: 20px;
    line-height: 30px;
    letter-spacing: 0.3px;
    color: var(--ink-slate);
    white-space: nowrap;
  }
  .contact-label {
    color: var(--brand-red);
    font-weight: 700;
    margin-right: 8px;
  }
</style>
</head>
<body>
  <section class="card" aria-label="Business card">
    <p class="company"><span class="company-mark"></span>Birch Property Developments</p>
    <div class="name-line">
      <h1 class="first-name">Lachlan</h1>
      <div class="surname-group">
        <span class="surname">VOSS</span>
        <span class="job-title">Manager/Director</span>
      </div>
    </div>
    <div class="accent-rule"></div>
    <address class="contact">
      Po Box 4657<br>
      Thuringowa Central Qld<br>
      <span class="contact-label">P</span>0455 386 218<br>
      <span class="contact-label">E</span>lachlan@birchpropertydevelopments
    </address>
  </section>
</body>
</html>
```